Professional Modern Website Design

We are a premium IT services provider to the financial industry based in London. Our company is called Velmar our current holding page is www.velmar.co.uk. We require a new website to match our new corporate identity. This project is for the design phase only. Development will be handled in-house. I have attached examples of wire frames we have developed (although open to suggestions for improvement) Our brand document that should demonstrate current brand, inc how we communicate to potential clients and finally mostly completed web-content.
We are looking for designers that can create something that sets us apart from our competitors.
Target Market(s)
IT Decision makers in Finance companies such as; hedge funds, private investment banks etc
Industry/Entity Type
Financial
Number of Pages Required
5+ page
Requirements
Must have
- hexagon elements in the design, unique design.
Nice to have
- Blog and social media feeds
Should not have
- Should not resemble a downloaded template

```html
<!DOCTYPE html>
<html lang="en">
<head>
<meta charset="utf-8">
<title>Velmar – Integrated IT for Finance</title>
<link href="https://fonts.googleapis.com/css2?family=Oswald:wght@300;400&family=Raleway:wght@500;600&family=Open+Sans:wght@400;600;700&display=swap" rel="stylesheet">
<style>
:root{
  --orange:#e8662a;
  --orange-dark:#c9521c;
  --ink:#2d2d2d;
  --grey:#666;
  --light:#f1f1f1;
  --line:#dcdcdc;
  --black:#050505;
  --footer:#383838;
  --footer-dark:#222;
  --white:#fff;
}
*{box-sizing:border-box;margin:0;padding:0}
html,body{width:1200px;height:3673px;overflow:hidden}
body{position:relative;font-family:"Open Sans",sans-serif;color:var(--ink);background:var(--white)}
.abs{position:absolute}
.section-title{position:absolute;left:0;width:1200px;text-align:center;font-family:"Raleway",sans-serif;font-weight:600;font-size:26px;letter-spacing:1px;color:var(--orange);text-transform:uppercase}

/* hero */
.hero{position:absolute;left:0;top:0;width:1200px;height:730px;background:linear-gradient(180deg,#1d1d1f 0%,#3a332e 40%,#5a4636 62%,#2a2422 100%)}
.hero-photo{position:absolute;inset:0;background:radial-gradient(ellipse at 60% 80%,rgba(232,140,70,.35),transparent 55%),linear-gradient(90deg,rgba(0,0,0,.55),rgba(0,0,0,.1) 50%,rgba(0,0,0,.5))}
.nav a{position:absolute;top:74px;font-family:"Open Sans",sans-serif;font-size:15px;color:var(--white);text-decoration:none;letter-spacing:.5px}
.nav a.active{color:var(--orange)}
.brand{position:absolute;left:540px;top:52px;width:120px;text-align:center;font-family:"Open Sans",sans-serif;font-weight:700;font-size:22px;color:var(--orange);letter-spacing:1px}
.brand i{display:block;width:14px;height:14px;background:var(--orange);margin:0 auto 6px}
.dropdown{position:absolute;left:387px;top:152px;width:300px;height:166px;background:rgba(0,0,0,.55);border-left:1px solid rgba(255,255,255,.25);padding:14px 0 0 38px}
.dropdown li{list-style:none;font-size:13px;color:var(--white);line-height:28px;position:relative}
.dropdown li:before{content:"";position:absolute;left:-16px;top:11px;border-left:6px solid var(--white);border-top:4px solid transparent;border-bottom:4px solid transparent}
.hero h1{position:absolute;left:196px;top:366px;font-family:"Oswald",sans-serif;font-weight:400;font-size:40px;color:var(--white);text-transform:uppercase;letter-spacing:.5px}
.hero p{position:absolute;left:180px;top:430px;width:840px;font-family:"Oswald",sans-serif;font-weight:300;font-size:24px;line-height:38px;color:var(--white);text-transform:uppercase;text-align:center}
.btn{position:absolute;left:497px;top:578px;width:206px;height:59px;background:var(--orange);color:var(--white);font-family:"Oswald",sans-serif;font-size:26px;line-height:59px;text-align:center;border-bottom:3px solid var(--orange-dark)}
.arrow{position:absolute;top:430px;width:22px;height:44px}

/* who */
.intro{position:absolute;left:110px;top:824px;width:980px;text-align:center;font-size:14px;line-height:24px;color:var(--grey)}
.role{position:absolute;top:940px;width:250px;text-align:center}
.hex-photo{width:210px;height:236px;margin:0 auto;background:#f6e4d8;clip-path:polygon(50% 0,100% 25%,100% 75%,50% 100%,0 75%,0 25%);padding:8px}
.hex-photo div{width:100%;height:100%;clip-path:polygon(50% 0,100% 25%,100% 75%,50% 100%,0 75%,0 25%);background:linear-gradient(180deg,#d9dde3,#8d97a6 60%,#3a4250)}
.role h3{margin-top:22px;font-size:14px;font-weight:700;color:var(--orange)}
.role p{margin-top:14px;font-size:11px;line-height:19px;color:var(--grey);text-align:justify;text-align-last:center}

/* services */
.services{position:absolute;left:0;top:1482px;width:1200px;height:453px;background:linear-gradient(180deg,#e4e4e4 0%,#cfcfcf 55%,#bdbdbd 100%)}
.service{position:absolute;width:330px}
.hex-icon{position:absolute;width:76px;height:86px;background:#2f2f2f;clip-path:polygon(50% 0,100% 25%,100% 75%,50% 100%,0 75%,0 25%)}
.hex-icon.on{background:var(--orange)}
.hex-icon svg{position:absolute;left:22px;top:27px}
.service h4{margin-left:90px;font-size:13px;font-weight:700;text-transform:uppercase;color:var(--ink)}
.service h4.on{color:var(--orange)}
.service p{margin:6px 0 0 90px;font-size:13px;line-height:22px;color:var(--ink);width:240px}

/* process */
.process{position:absolute;left:0;top:1935px;width:1200px;height:509px;background:var(--black)}
.process .section-title{color:var(--white)}
.step{position:absolute;top:158px;width:300px;text-align:center}
.step h4{position:absolute;top:218px;width:300px;font-size:14px;font-weight:700;color:var(--orange);text-transform:uppercase}
.step p{position:absolute;top:246px;width:300px;font-size:13px;line-height:22px;color:var(--white)}

/* partners */
.partners{position:absolute;left:0;top:2444px;width:1200px;height:365px;background:var(--light)}
.partners p{position:absolute;left:250px;top:102px;width:700px;text-align:center;font-size:13.5px;line-height:24px;color:#444}
.partner{position:absolute;top:248px;font-size:22px;font-weight:600;color:#777;transform:translateX(-50%)}

/* blog */
.blog-head{position:absolute;font-family:"Raleway",sans-serif;font-weight:600;font-size:19px;color:var(--orange);text-transform:uppercase;letter-spacing:.5px}
.post{position:absolute;left:90px;width:694px;height:180px;border:1px solid var(--line);background:var(--white)}
.post .thumb{position:absolute;left:12px;top:14px;width:166px;height:150px}
.post h5{position:absolute;left:203px;top:14px;font-family:"Raleway",sans-serif;font-weight:500;font-size:17px;color:var(--ink)}
.meta{position:absolute;left:203px;top:56px;font-size:11px;color:var(--grey)}
.meta b{color:var(--orange);font-weight:400}
.post p{position:absolute;left:203px;top:84px;width:470px;font-size:10.5px;line-height:21px;color:var(--grey)}
.post p b{color:var(--orange);font-weight:600}
.tweets{position:absolute;left:820px;top:2890px;width:290px;height:363px;border:1px solid var(--line)}
.tweet{position:absolute;left:14px;width:262px}
.tweet i{position:absolute;left:0;top:0;width:48px;height:48px;background:#333;border:1px solid var(--line)}
.tweet i:after{content:"";position:absolute;left:14px;top:14px;width:18px;height:18px;background:var(--orange)}
.tweet p{margin-left:64px;font-size:10.5px;line-height:17px;color:var(--grey)}
.tweet p b{color:var(--orange);font-weight:400}
.tweet em{display:block;margin-left:64px;font-size:10.5px;color:#444;margin-top:4px}

/* footer */
.band{position:absolute;left:0;top:3301px;width:1200px;height:86px;background:#262626;text-align:center;line-height:86px;font-family:"Raleway",sans-serif;font-size:19px;letter-spacing:3px;color:var(--white)}
.band span{color:var(--orange)}
.footer{position:absolute;left:0;top:3387px;width:1200px;height:225px;background:linear-gradient(180deg,#4a4a4a,#333)}
.footer h6{position:absolute;top:38px;font-family:"Raleway",sans-serif;font-weight:500;font-size:17px;color:var(--orange)}
.footer p{position:absolute;font-size:10.5px;line-height:17px;color:#ddd}
.social{position:absolute;top:160px;width:28px;height:28px;border-radius:50%;background:#3b8ed0}
.contact-row{position:absolute;left:892px;font-size:10.5px;color:#ddd}
.contact-row b{display:inline-block;width:70px;font-weight:600}
.bottom{position:absolute;left:0;top:3612px;width:1200px;height:61px;background:var(--footer-dark);font-size:11px;color:#bbb;line-height:61px}
.bottom .links{position:absolute;left:90px;word-spacing:8px}
.bottom .copy{position:absolute;right:90px}
</style>
</head>
<body>

<section class="hero">
  <div class="hero-photo" role="img" aria-label="Night city street with light trails and office towers"></div>
  <nav class="nav">
    <a style="left:116px">HOME</a>
    <a style="left:258px">ABOUT</a>
    <a class="active" style="left:405px">SERVICES</a>
    <a style="left:696px">PARTNERS</a>
    <a style="left:872px">CLIENTS</a>
    <a style="left:1032px">CONTACT</a>
  </nav>
  <div class="brand"><i></i>VELMAR</div>
  <ul class="dropdown">
    <li>Data Centre &amp; Infrastructure</li>
    <li>Support, Managed &amp; Professional Services</li>
    <li>Voice &amp; Data Networks</li>
    <li>Hosting &amp; Cloud</li>
    <li>Security &amp; IRM</li>
  </ul>
  <svg class="arrow" style="left:38px" viewBox="0 0 22 44"><path d="M20 2 2 22l18 20" fill="none" stroke="#fff" stroke-opacity=".6" stroke-width="2"/></svg>
  <svg class="arrow" style="left:1140px" viewBox="0 0 22 44"><path d="M2 2l18 20L2 42" fill="none" stroke="#fff" stroke-opacity=".6" stroke-width="2"/></svg>
  <h1>You need integration. We're always there with you</h1>
  <p>Velmar is one of the leading systems integrators to the world's finance sector. We are an extension of your business and our services portfolio has been built so you always have access to a complete partner.</p>
  <div class="btn">ABOUT US</div>
</section>

<h2 class="section-title" style="top:776px">Who are you?</h2>
<p class="intro">Lorem Ipsum has been the industry's standard dummy text ever since the 1500s, when an unknown printer took a galley of type and scrambled it to make a type specimen book. It has survived not only five centuries, but also the leap into electronic typesetting, remaining essentially unchanged. It was popularised in the 1960s with the release of Lettra sheets containing Lorem Ipsum passages, and more recently with desktop publishing software</p>

<div class="role" style="left:83px">
  <div class="hex-photo"><div role="img" aria-label="Portrait of a smiling senior executive in a suit"></div></div>
  <h3>Senior Hedge Fund Manager/CEO</h3>
  <p>You need to develop and implement strategies for business growth, while ensuring profitability. You're aware your biggest asset is your staff and a happy workforce is a productive one. Security is a key concern in a changing always-on world and you need to be compliant, but you don't want to overspend. Velmar can help you find the best solutions to help your business grow at the speed you want it to.</p>
</div>
<div class="role" style="left:350px">
  <div class="hex-photo"><div role="img" aria-label="Portrait of a finance director in a suit"></div></div>
  <h3>CFO</h3>
  <p>Your key responsibility is to obtain the maximum ROI from products and services. You understand investment opportunities, providing they return higher efficiencies and revenues. You are concerned more with long-term spending versus short-term and how you can get the most value out of a proposition. Velmar can advise how to boost ROI by streamlining your business to maximise return.</p>
</div>
<div class="role" style="left:617px">
  <div class="hex-photo"><div role="img" aria-label="Technology officer standing with arms crossed"></div></div>
  <h3>CTO</h3>
  <p>Integration with partners and services is your key concern. You want to make sure any IT system you implement will work with the whole infrastructure of your company. You don't want your team to waste valuable time dealing with things that don't matter. Velmar provides the whole picture to ensure your company is ready for the next generation of IT.</p>
</div>
<div class="role" style="left:882px">
  <div class="hex-photo"><div role="img" aria-label="Young employee in a shirt and tie"></div></div>
  <h3>Employees</h3>
  <p>You're working hard, but not getting anywhere fast. You want the tools to make your job easier so you can spend more time thinking about what you're doing rather than how you're doing it. You shouldn't have to think about the technology you're using, because it should just work. Velmar can help you get back on track everyday.</p>
</div>

<section class="services" role="img" aria-label="Faded grey city skyline behind the services list">
  <h2 class="section-title" style="top:44px">Our services</h2>
  <div class="service" style="left:84px;top:128px">
    <div class="hex-icon on"><svg width="32" height="32" viewBox="0 0 32 32" fill="#fff"><rect x="4" y="6" width="24" height="6"/><rect x="4" y="14" width="24" height="6"/><rect x="4" y="22" width="24" height="6"/></svg></div>
    <h4 class="on">Data Centre &amp; Infrastructure</h4>
    <p>Lorem Ipsum is simply dummy text of the printing and typesetting industry. Lorem Ipsum has been the industry's...</p>
  </div>
  <div class="service" style="left:437px;top:128px">
    <div class="hex-icon"><svg width="32" height="32" viewBox="0 0 32 32" fill="#fff"><circle cx="16" cy="9" r="6"/><path d="M5 30c0-8 5-12 11-12s11 4 11 12z"/></svg></div>
    <h4>Professional Services</h4>
    <p>Lorem Ipsum is simply dummy text of the printing and typesetting industry. Lorem Ipsum has been the industry's...</p>
  </div>
  <div class="service" style="left:800px;top:128px">
    <div class="hex-icon"><svg width="32" height="32" viewBox="0 0 32 32" fill="none" stroke="#fff" stroke-width="2.5"><rect x="7" y="3" width="18" height="26"/><path d="M11 10h10M11 16h10M11 22h6"/></svg></div>
    <h4>Voice and Data</h4>
    <p>Lorem Ipsum is simply dummy text of the printing and typesetting industry. Lorem Ipsum has been the industry's...</p>
  </div>
  <div class="service" style="left:266px;top:276px">
    <div class="hex-icon"><svg width="32" height="32" viewBox="0 0 32 32" fill="#fff"><path d="M8 26a6 6 0 0 1 0-12 9 9 0 0 1 17 2 5 5 0 0 1 0 10z"/></svg></div>
    <h4>Hosting and Cloud</h4>
    <p>Lorem Ipsum is simply dummy text of the printing and typesetting industry. Lorem Ipsum has been the industry's...</p>
  </div>
  <div class="service" style="left:616px;top:276px">
    <div class="hex-icon"><svg width="32" height="32" viewBox="0 0 32 32" fill="#fff"><path d="M10 14V10a6 6 0 0 1 12 0v4h-3v-4a3 3 0 0 0-6 0v4z"/><rect x="6" y="14" width="20" height="15"/></svg></div>
    <h4>Security and IRM</h4>
    <p>Lorem Ipsum is simply dummy text of the printing and typesetting industry. Lorem Ipsum has been the industry's...</p>
  </div>
</section>

<section class="process">
  <h2 class="section-title" style="top:40px;color:#fff">Our process</h2>
  <svg class="abs" style="left:0;top:0" width="1200" height="509">
    <line x1="350" y1="215" x2="850" y2="215" stroke="#666" stroke-width="1.5"/>
    <circle cx="411" cy="215" r="5" fill="#e8662a"/>
    <circle cx="789" cy="215" r="5" fill="#e8662a"/>
    <polygon points="225,75 345,145 345,285 225,355 105,285 105,145" fill="#e8662a"/>
    <polygon points="600,75 720,145 720,285 600,355 480,285 480,145" fill="none" stroke="#9a9a9a" stroke-width="2"/>
    <polygon points="975,75 1095,145 1095,285 975,355 855,285 855,145" fill="none" stroke="#9a9a9a" stroke-width="2"/>
    <g fill="none" stroke="#fff" stroke-width="7" stroke-linejoin="round">
      <path d="M195 260l8-26 46-46 18 18-46 46z"/><path d="M236 200l18 18"/>
    </g>
    <path d="M565 225l70-35-22 70-14-20-14 16v-20z" fill="#fff"/>
    <g fill="none" stroke="#fff" stroke-width="8"><rect x="935" y="180" width="80" height="54"/></g>
    <rect x="955" y="244" width="40" height="7" fill="#fff"/>
  </svg>
  <div class="step" style="left:75px"><h4>Analysis &amp; Assessment</h4><p>Lorem Ipsum has been the industry's standard dummy text ever since the 1500s, when an unknown printer took a galley of</p></div>
  <div class="step" style="left:450px"><h4>Implementation</h4><p>Lorem Ipsum has been the industry's standard dummy text ever since the 1500s, when an unknown printer took a galley of type and</p></div>
  <div class="step" style="left:825px"><h4>Adapt and Glow</h4><p>Lorem Ipsum has been the industry's standard dummy text ever since the 1500s, when an unknown printer took a galley of type and</p></div>
</section>

<section class="partners">
  <h2 class="section-title" style="top:52px">Our partners</h2>
  <p>We have carefully selected our partners to help your business grow how you want it to. All our partners have the same values as we do, making sure their solutions seamlessly integrate with your organisation.</p>
  <span class="partner" style="left:215px">Harlow</span>
  <span class="partner" style="left:416px">Corvane</span>
  <span class="partner" style="left:625px">Mirosta</span>
  <span class="partner" style="left:798px">Veltrix</span>
  <span class="partner" style="left:985px">Lunara</span>
</section>

<h3 class="blog-head" style="left:88px;top:2850px">Latest blog</h3>
<svg class="abs" style="left:758px;top:2856px" width="26" height="12"><path d="M6 1 1 6l5 5M20 1l5 5-5 5" fill="none" stroke="#888" stroke-width="1.5"/></svg>
<h3 class="blog-head" style="left:820px;top:2850px">Live feeds</h3>

<article class="post" style="top:2893px">
  <div class="thumb" role="img" aria-label="Businessman in a field under blue sky" style="background:linear-gradient(180deg,#7fb1de,#cfe2f2 55%,#8aa45a)"></div>
  <h5>Cloud computing and the future of flexible working</h5>
  <div class="meta">Published in <b>Photography</b> &nbsp;&nbsp; Written by <b>Admin</b> &nbsp;&nbsp; Comments <b>377</b></div>
  <p>Velmar is one of the leading systems integrators to the world's financial sector. We have more than 40 years' experience working with high profile financial organisations. We always strive for mutual growth, then your footprint against your competition... <b>MORE INFO</b></p>
</article>
<article class="post" style="top:3089px">
  <div class="thumb" role="img" aria-label="Businessman juggling office tasks" style="background:linear-gradient(180deg,#b9bcc0,#6e737a)"></div>
  <h5>EU Wants To Make Cloud Computing Greener</h5>
  <div class="meta">Published in <b>Photography</b> &nbsp;&nbsp; Written by <b>Admin</b> &nbsp;&nbsp; Comments <b>377</b></div>
  <p>Velmar is one of the leading systems integrators to the world's financial sector. We have more than 40 years' experience working with high profile financial organisations. We always strive for mutual growth, then your footprint against your competition... <b>MORE INFO</b></p>
</article>

<aside class="tweets">
  <div class="tweet" style="top:22px"><i></i><p>It is a long established fact that reader will be distracted <b>http://velmar.ly/bg01</b></p><em>24 minutes ago</em></div>
  <div class="tweet" style="top:136px"><i></i><p>It is a long established fact that reader will be distracted <b>http://velmar.ly/bg01</b></p><em>24 minutes ago</em></div>
  <div class="tweet" style="top:250px"><i></i><p>It is a long established fact that reader will be distracted <b>http://velmar.ly/bg01</b></p><em>24 minutes ago</em></div>
</aside>

<div class="band"><span>INTEGRATED</span> PARTNERSHIPS</div>

<footer class="footer">
  <h6 style="left:98px">Stay in Touch!</h6>
  <p style="left:98px;top:80px;width:160px">Follow US in our social networks! Lorem ipsum dolor sit amet consectetur and adipiscing elit.</p>
  <span class="social" style="left:98px"></span>
  <span class="social" style="left:134px"></span>
  <span class="social" style="left:170px;background:#d9483b"></span>
  <span class="social" style="left:206px;background:#1e77b5"></span>

  <h6 style="left:358px">40 years of experience</h6>
  <svg class="abs" style="left:358px;top:80px" width="46" height="52"><polygon points="23,1 45,13 45,39 23,51 1,39 1,13" fill="#fff"/><text x="23" y="30" text-anchor="middle" font-family="Open Sans,sans-serif" font-weight="700" font-size="14" fill="#e8662a">40</text></svg>
  <p style="left:412px;top:80px;width:140px">Lorem Ipsum has been the industry's standard dummy text ever since the 1500s, when an unknown printer took a galley</p>

  <h6 style="left:630px">Location</h6>
  <div class="abs" role="img" aria-label="Street map of Mayfair with a location pin" style="left:630px;top:80px;width:180px;height:110px;background:linear-gradient(135deg,#e9e6df,#cfcac0)"></div>

  <h6 style="left:892px">Contact Us</h6>
  <div class="contact-row" style="top:80px"><b>Adress:</b>24 Harrow Lane, Mayfair,<br><b></b>London W1 4AB</div>
  <div class="contact-row" style="top:132px"><b>Phone:</b>+44 20 7946 0123</div>
  <div class="contact-row" style="top:160px"><b>Email:</b><span style="color:#e8662a">info@velmar.co.uk</span></div>
</footer>

<div class="bottom">
  <span class="links">HOME / ABOUT US / SERVICES / PARTNERS / CLIENTS / CONTACT US</span>
  <span class="copy">© Copyright 2015 Velmar All Rights Reserved</span>
</div>

</body>
</html>
```